Employees at T&M Gale Power Solutions need new modern business cards

We need new business cards that showcase our new rebranded logo. We are seeking modern, clean, fresh, attractive cards while still being professional. We want to stand out. A little bit about us: we work in Canada and the USA. We offer Technical Field Advisors to support wind turbine manufacturers through the construction phase of wind farms. I am attaching a mock inspiration picture to lead you in the direction we want to see this go. Also, FYI We have approx. 10/11 different employees that would need their own card. Let me know when you would need everyone's name. We would love to see some black and white options as well as color copies- when using colors we want green to be the dominant color with accents for blue and orange (colors should match our logo). I have also attached copies of our old business card for reference.

Contact Information for Business Card

Name, Telephone, Email, address, company name, website. EXAMPLE: Hugh Marlow, HughMarlow@tandmgale.example, 555-381-4926, 217763 Birch Line #9, Elmhurst, ON X1Y 2Z3, www.tandmgale.example

Colors
0054AA
0677BA
7BADD7
CADEEF
E8F1F8
00AB8E
00BBA5
67D7C9
C6EFE9
E9F9F6
F0912C
F2A743
F7CA91
FBE8D2
FDF5EE

Requirements
Must have
• 2 sided business card

```html
<!DOCTYPE html>
<html lang="en">
<head>
<meta charset="utf-8">
<title>T&amp;M Gale Power Solutions – Business Card</title>
<link rel="stylesheet" href="https://fonts.googleapis.com/css2?family=Ubuntu:wght@400;500;700&family=Open+Sans:wght@400;600&display=swap">
<style>
  :root {
    --stage: #2a2d33;
    --card-white: #ffffff;
    --card-black: #0d0d0f;
    --pattern-light: #1c1c20;
    --brand-blue: #0677ba;
    --brand-green: #3aaa45;
    --brand-orange: #f0912c;
    --ink: #222326;
    --rule: #9a9a9a;
  }
  * { margin: 0; padding: 0; box-sizing: border-box; }
  html, body { width: 1200px; height: 900px; overflow: hidden; }
  body {
    background: var(--stage);
    display: flex;
    align-items: center;
    justify-content: center;
    gap: 40px;
  }
  .card {
    position: relative;
    width: 560px;
    height: 320px;
    overflow: hidden;
    border-radius: 4px;
  }
  .card--front { background: var(--card-white); }
  .card--back { background: var(--card-black); }
  .card__bands { position: absolute; inset: 0; }

  .brand {
    position: absolute;
    left: 44px;
    top: 104px;
    display: flex;
    align-items: center;
    gap: 10px;
  }
  .brand__dot {
    width: 30px; height: 30px;
    border-radius: 50%;
    background: var(--brand-green);
    flex: none;
  }
  .brand__name {
    font-family: "Ubuntu", sans-serif;
    font-weight: 700;
    font-size: 16px;
    line-height: 1.2;
    color: var(--brand-green);
    letter-spacing: 0.4px;
    text-transform: uppercase;
  }
  .divider {
    position: absolute;
    left: 282px;
    top: 92px;
    width: 1.5px;
    height: 118px;
    background: var(--rule);
  }
  .contact {
    position: absolute;
    left: 302px;
    top: 92px;
    font-family: "Open Sans", sans-serif;
    color: var(--ink);
    font-size: 12.5px;
    line-height: 1.45;
  }
  .contact__name {
    font-family: "Ubuntu", sans-serif;
    font-weight: 500;
    font-size: 20px;
    color: var(--brand-blue);
    text-transform: uppercase;
    letter-spacing: 0.5px;
    margin-bottom: 6px;
  }
  .contact__address { margin-bottom: 8px; }
  .contact__line { display: flex; align-items: center; gap: 7px; }
  .contact__icon { width: 11px; height: 11px; flex: none; }

  .back__pattern {
    position: absolute;
    inset: 0;
    background: radial-gradient(ellipse at 40% 40%, var(--pattern-light) 0%, var(--card-black) 75%);
  }
  .back__brand {
    position: absolute;
    left: 300px;
    top: 176px;
    display: flex;
    align-items: center;
    gap: 8px;
  }
  .back__dot {
    width: 18px; height: 18px;
    border-radius: 50%;
    background: var(--brand-green);
    flex: none;
  }
  .back__name {
    font-family: "Ubuntu", sans-serif;
    font-weight: 700;
    font-size: 12px;
    color: var(--brand-green);
    text-transform: uppercase;
    letter-spacing: 0.6px;
  }
</style>
</head>
<body>
  <section class="card card--front">
    <svg class="card__bands" viewBox="0 0 560 320" width="560" height="320" aria-hidden="true">
      <polygon points="0,198 136,250 0,230" fill="var(--brand-orange)"/>
      <polygon points="0,228 200,266 0,294" fill="var(--brand-green)"/>
      <polygon points="0,292 560,262 560,320 0,320" fill="var(--brand-blue)"/>
    </svg>

    <div class="brand">
      <span class="brand__dot"></span>
      <p class="brand__name">T&amp;M Gale<br>Power Solutions</p>
    </div>

    <div class="divider"></div>

    <div class="contact">
      <h1 class="contact__name">Hugh Marlow</h1>
      <p class="contact__address">217763 Birch Line #9<br>Elmhurst, ON X1Y 2Z3</p>
      <p class="contact__line">
        <svg class="contact__icon" viewBox="0 0 12 12" aria-hidden="true"><path d="M2.5 1h2l1 3-1.3 1a6 6 0 0 0 2.8 2.8l1-1.3 3 1v2a1 1 0 0 1-1 1A9.5 9.5 0 0 1 1.5 2a1 1 0 0 1 1-1z" fill="var(--brand-orange)"/></svg>
        555-381-4926
      </p>
      <p class="contact__line">
        <svg class="contact__icon" viewBox="0 0 12 12" aria-hidden="true"><rect x="0.5" y="2" width="11" height="8" rx="1" fill="var(--brand-orange)"/><path d="M1 2.8 6 6.5l5-3.7" stroke="#fff" stroke-width="1" fill="none"/></svg>
        HughMarlow@tandmgale.example
      </p>
      <p class="contact__line">
        <svg class="contact__icon" viewBox="0 0 12 12" aria-hidden="true"><circle cx="6" cy="6" r="5.3" fill="var(--brand-orange)"/><path d="M0.7 6h10.6M6 0.7c-2.6 3-2.6 7.6 0 10.6M6 0.7c2.6 3 2.6 7.6 0 10.6" stroke="#fff" stroke-width="0.8" fill="none"/></svg>
        www.tandmgale.example
      </p>
    </div>
  </section>

  <section class="card card--back">
    <div class="back__pattern" role="img" aria-label="Faint embossed repeat pattern of the company emblem across a black card"></div>
    <div class="back__brand">
      <span class="back__dot"></span>
      <p class="back__name">T&amp;M Gale Power Solutions</p>
    </div>
  </section>
</body>
</html>
```